Spy/Espionage/Counterintelligence Membership Community Needs a PowerPoint Template

We need a powerpoint template for one of our business verticals focused on spies, espionage, and counterintelligence. The name of it is "Amber Harbor Guild" and the logo is attached. Amber Harbor Guild is a community that connects people with experts in espionage and counterintelligence through an online social network, as well as in-person events. We would like to see designs that incorporate the red and black of the logo. The design should communicate mystery/suspense and peak curiosity.

Target Market(s)

Late 20s to baby boomers, male

Industry/Entity Type

Social Club

Font styles to use
Sans Serif

Colors
ec1f27
000000
ffffff

Requirements
Must have
• A user-friendly ppt template file. Incorporate basic fonts that don't have to be installed on every computer for presentations. A cover slide and a basic inside slide. A white background. I will also need graphic source files.
Nice to have
• Plenty of space for slide title and body content. Logo on every slide.
Should not have
• Inconsistency with fonts. Misalignment of images.

```html
<!DOCTYPE html>
<html lang="en">
<head>
<meta charset="utf-8">
<title>Project Title Here</title>
<link href="https://fonts.googleapis.com/css2?family=Didact+Gothic&family=Open+Sans:wght@600&family=Roboto:wght@400;500&display=swap" rel="stylesheet">
<style>
  :root {
    --brand-red: #c40000;
    --header-red: #c70000;
    --ink: #1a1a1a;
    --muted: #8f8f8f;
    --row-grey: #e2e2e2;
    --row-pink: #fbdede;
    --footer: #1b1b1b;
    --white: #ffffff;
  }
  * { box-sizing: border-box; margin: 0; padding: 0; }
  html, body { width: 1200px; height: 900px; overflow: hidden; background: var(--white); }
  .slide { position: relative; width: 1200px; height: 900px; background: var(--white); }

  .title-bar {
    position: absolute; left: 0; top: 0; width: 1200px; height: 75px;
    background: var(--brand-red);
    border-bottom: 3px solid var(--ink);
    display: flex; align-items: center; justify-content: space-between;
    padding: 0 22px 0 20px;
  }
  .project-title {
    font-family: "Didact Gothic", sans-serif; color: var(--white);
    font-size: 45px; font-weight: 400; letter-spacing: 0.5px;
  }
  .brand { display: flex; align-items: center; gap: 10px; }
  .brand-dot { width: 40px; height: 40px; border-radius: 50%; background: var(--ink); }
  .brand-name { font-family: "Didact Gothic", sans-serif; font-size: 30px; color: var(--ink); }

  .section-heading {
    position: absolute; left: 64px; top: 148px;
    font-family: "Roboto", sans-serif; font-weight: 500; font-size: 22px; color: var(--brand-red);
  }
  .intro {
    position: absolute; left: 73px; top: 191px; width: 1080px;
    display: grid; grid-template-columns: 366px 366px 348px;
    font-family: "Roboto", sans-serif; font-size: 17.5px; line-height: 24px; color: var(--muted);
  }

  .data-table {
    position: absolute; left: 72px; top: 301px; width: 1008px;
    border-collapse: separate; border-spacing: 0 4.5px; margin-top: -4.5px;
    font-family: "Roboto", sans-serif;
  }
  .data-table th {
    background: var(--header-red); color: var(--white);
    font-family: "Open Sans", sans-serif; font-weight: 600; font-size: 25px;
    height: 60px; text-align: left; text-transform: uppercase;
  }
  .data-table td { height: 60px; font-size: 19px; color: var(--ink); }
  .data-table tr:nth-child(odd) td { background: var(--row-grey); }
  .data-table tr:nth-child(even) td { background: var(--row-pink); }
  .col-a { padding-left: 21px; width: 336px; }
  .col-b { padding-left: 24px; width: 391px; }
  .col-c { padding-left: 8px; }
  th.col-a { padding-left: 21px; }
  th.col-b { padding-left: 31px; }
  th.col-c { padding-left: 14px; }

  .footer-bar {
    position: absolute; left: 0; bottom: 0; width: 1200px; height: 44px;
    background: var(--footer); display: flex; align-items: center; justify-content: space-between;
    padding: 0 9px 0 10px;
  }
  .copyright { font-family: "Didact Gothic", sans-serif; font-size: 21px; color: var(--white); }
  .page-number {
    width: 34px; height: 34px; border-radius: 50%;
    background: var(--brand-red); border: 2px solid var(--white);
    color: var(--white); font-family: "Roboto", sans-serif; font-size: 19px;
    display: flex; align-items: center; justify-content: center;
  }
</style>
</head>
<body>
<div class="slide">
  <header class="title-bar">
    <h1 class="project-title">Project Title Here</h1>
    <div class="brand">
      <span class="brand-dot"></span>
      <span class="brand-name">Amber Harbor Guild</span>
    </div>
  </header>

  <h2 class="section-heading">Table Head Here</h2>
  <div class="intro">
    <p>Lorem ipsum dolor sit Lorem ipsum dolor sit Lorem ipsum dolor sit Lorem ipsum dolor sit Lorem ipsum dolor sit Lorem ipsum dolor sit</p>
    <p>Lorem ipsum dolor sit Lorem ipsum dolor sit Lorem ipsum dolor sit Lorem ipsum dolor sit Lorem ipsum dolor sit Lorem ipsum dolor sit</p>
    <p>Lorem ipsum dolor sit Lorem ipsum dolor Lorem ipsum dolor sit Lorem ipsum dolor</p>
  </div>

  <table class="data-table">
    <thead>
      <tr><th class="col-a">Table Head Here</th><th class="col-b">Table Head Here</th><th class="col-c">Table Head Here</th></tr>
    </thead>
    <tbody>
      <tr><td class="col-a">Subtext here Subtext here</td><td class="col-b">Subtext here Subtext here</td><td class="col-c">Subtext here Subtext here</td></tr>
      <tr><td class="col-a">Subtext here Subtext here</td><td class="col-b">Subtext here Subtext here</td><td class="col-c">Subtext here Subtext here</td></tr>
      <tr><td class="col-a">Subtext here Subtext here</td><td class="col-b">Subtext here Subtext here</td><td class="col-c">Subtext here Subtext here</td></tr>
      <tr><td class="col-a">Subtext here Subtext here</td><td class="col-b">Subtext here Subtext here</td><td class="col-c">Subtext here Subtext here</td></tr>
      <tr><td class="col-a">Subtext here Subtext here</td><td class="col-b">Subtext here Subtext here</td><td class="col-c">Subtext here Subtext here</td></tr>
      <tr><td class="col-a">Subtext here Subtext here</td><td class="col-b">Subtext here Subtext here</td><td class="col-c">Subtext here Subtext here</td></tr>
    </tbody>
  </table>

  <footer class="footer-bar">
    <span class="copyright">Copyright text here</span>
    <span class="page-number">1</span>
  </footer>
</div>
</body>
</html>
```